Price list for young Relaxon clinic

I require a price list/Treatment menu for clinic

To include:
Logo
Address
Phone number
Website

List of services and Prices
Relaxon 1 area £100
Relaxon 2 areas £150
Relaxon 3 areas £200
Lip Enhancement 0.5ml £100
Lip Enhancement 1ml £200
Facial Fillers £200 per 1ml
Volumiq £450 per session (2 vials - must be bought as a course)
Non Surgical Face Lift (Thread Lift) £600 per area
Skin Press Full Face £250
Skin Press Small Per Small Area £100
Cryo Therapy £60
Chemical Peel Light Peel and Microdermabrasion £85
Chemical Peel Deep Peel £150
Consultation £30 redeemable against service
Relaxon Top Up Relaxon £50 (must be within 2 weeks of 1st treatment)
Filler Top Up £100 (must be within 2 weeks of 1st appointment)

Open Hours
Updates

Company Name: HVM Address: 482 Pellbrook Road, 6 Warnford High Street, KT4 3JQ Phone: 0208 947 2186 Website: www.hollyvanmereaesthetics.co.uk

Please add more colour

Needs to be much cleaner and simpler Front page to include logo and price list Back page to inculde open hours and contact information including google map. Please no images with needles. Images of lips and faces are good, but try not to crowd copy on the pagei. No copy on top of images. White, grey, black and reds are good on colouring.

Target Market(s)

young market ages 22-45 years old mainly female
modern

Industry/Entity Type

Clinic

Number of Pages Required

4 page

Requirements
Must have
• Logo - logo must be in colour grey/silver
• Address (small map?)
• Phone number
• Web address
• Services
• Open hours
• Prices
• Images

```html
<!DOCTYPE html>
<html lang="en">
<head>
<meta charset="utf-8">
<title>Holly Vanmere Aesthetics – Price List</title>
<link rel="stylesheet" href="https://fonts.googleapis.com/css2?family=Lato:wght@400;700&family=Libre+Baskerville:wght@400;700&display=swap">
<style>
  :root{
    --page-bg:#d9d6d0;
    --header-top:#444546;
    --header-bottom:#1f2021;
    --navy:#0e3a6e;
    --teal:#2fcdb3;
    --ink:#222;
    --note:#1f4f8f;
    --body-top:#ffffff;
    --body-bottom:#e4e5e7;
    --white:#fff;
    --bullet:#4b9bd6;
  }
  *{box-sizing:border-box;margin:0;padding:0}
  html,body{width:907px;height:1200px;overflow:hidden;background:var(--page-bg)}
  body{position:relative;font-family:"Lato",Arial,sans-serif;color:var(--ink)}
  .flyer{position:absolute;left:99px;top:100px;width:714px;height:1000px;overflow:hidden;
    background:linear-gradient(var(--body-top),var(--body-bottom));box-shadow:0 4px 14px rgba(0,0,0,.35)}
  .abs{position:absolute}

  /* header */
  .header{left:0;top:0;width:714px;height:113px;background:linear-gradient(var(--header-top),var(--header-bottom))}
  .brand{left:82px;top:38px;display:flex;align-items:center;gap:10px;color:var(--white)}
  .brand-dot{flex:none;width:30px;height:30px;border-radius:50%;background:#b9babc}
  .brand-name{font-family:"Libre Baskerville",serif;font-weight:400;font-size:12px;letter-spacing:1.5px;line-height:16px}
  .social{right:100px;top:52px;color:var(--white);font-size:17px;display:flex;align-items:center;gap:12px}
  .social i{display:block;width:22px;height:22px;background:#9c9c9c;border-radius:3px}
  .rule{left:0;top:113px;width:714px;height:5px;border-top:2px solid var(--white);background:var(--navy)}

  /* hero */
  .hero{left:0;top:118px;width:714px;height:262px;background:linear-gradient(100deg,#cfe3ec 0%,#9dc4d8 30%,#e9d3c8 60%,#c59a83 100%)}
  .hero-band{left:0;top:380px;width:714px;height:130px;background:var(--teal);border-top:12px solid var(--navy)}
  .welcome{left:146px;top:360px;width:452px;height:126px;border-radius:8px;background:linear-gradient(#fff 45%,#d2d3d5);
    border:2px solid var(--white);box-shadow:0 2px 6px rgba(0,0,0,.35);text-align:center}
  .welcome-kicker{margin-top:6px;font-family:"Libre Baskerville",serif;font-weight:700;font-variant:small-caps;font-size:30px;color:var(--navy);letter-spacing:1px;line-height:38px}
  .welcome-title{font-weight:400;font-size:29px;color:#2a2a2a;letter-spacing:.5px;line-height:36px}
  .welcome-tag{font-family:"Libre Baskerville",serif;font-weight:700;font-size:18px;color:#222;margin-top:4px}

  /* tabs */
  .tab{background:var(--navy);color:var(--white);font-family:"Libre Baskerville",serif;font-weight:700;font-size:18px;
    border-radius:12px;box-shadow:0 2px 3px rgba(0,0,0,.4);border:2px solid var(--white);display:flex;align-items:center;justify-content:center}
  .tab-services{left:230px;top:497px;width:275px;height:37px}
  .tab-hours{left:16px;top:741px;width:186px;height:35px}

  /* lists */
  .price-list{list-style:none;font-size:11px}
  .price-list li{position:relative;padding-left:14px;height:18.8px;line-height:14px}
  .price-list li.tall{height:31px}
  .price-list li::before{content:"";position:absolute;left:0;top:3px;width:8px;height:8px;border-radius:50%;
    background:radial-gradient(circle,#fff 25%,var(--bullet) 30%)}
  .row{display:flex;align-items:baseline}
  .row .fill{flex:1;border-bottom:1px dotted #555;margin:0 2px;transform:translateY(-3px)}
  .note{display:block;color:var(--note);font-size:10.5px;line-height:12px}
  .list-left{left:22px;top:548px;width:290px}
  .list-right{left:357px;top:548px;width:330px}
  .hours-left{left:22px;top:791px;width:180px}
  .hours-right{left:213px;top:792px;width:120px}

  /* results strip */
  .results{left:377px;top:730px;width:335px;height:183px;border:5px solid var(--teal);border-radius:22px 22px 0 22px;background:var(--white);overflow:hidden}
  .results-labels{display:flex;height:16px;background:#d7d8da;font-size:10px}
  .results-labels span{flex:1;text-align:center;line-height:16px;border-left:1px solid #888}
  .results-labels span:first-child{border-left:0;text-align:left;padding-left:6px}
  .results-photo{height:162px;background:linear-gradient(90deg,#d8b092,#f0cfb5 30%,#e3bb9c 60%,#f1d2ba)}

  /* map */
  .map{left:38px;top:892px;width:172px;height:91px;border:4px solid var(--teal);border-radius:0 18px 0 18px;background:linear-gradient(135deg,#e9e6df,#d6d3cc);z-index:2}

  /* footer */
  .footer{left:0;top:925px;width:714px;height:75px;background:linear-gradient(var(--header-top),var(--header-bottom));color:var(--white);font-size:12px;font-weight:700}
  .contact{display:flex;gap:8px;align-items:flex-start;line-height:15px}
  .contact svg{flex:none;margin-top:2px}
  .c-phone{left:236px;top:8px}
  .c-address{left:236px;top:25px;width:220px}
  .c-web{left:480px;top:11px}
  .c-mail{left:480px;top:31px}
</style>
</head>
<body>
<main class="flyer">
  <header class="abs header">
    <div class="abs brand">
      <span class="brand-dot"></span>
      <div class="brand-name">HOLLY VANMERE<br>AESTHETICS</div>
    </div>
    <div class="abs social">Follow Us on <i></i></div>
  </header>
  <div class="abs rule"></div>

  <div class="abs hero" role="img" aria-label="Photo of a woman receiving a facial treatment from a clinician"></div>
  <div class="abs hero-band"></div>
  <section class="abs welcome">
    <p class="welcome-kicker">Welcome to</p>
    <h1 class="welcome-title">HOLLY VANMERE AESTHETICS</h1>
    <p class="welcome-tag">Achive a Fresh and beautiful You</p>
  </section>

  <h2 class="abs tab tab-services">List of services and Prices</h2>
  <ul class="abs price-list list-left">
    <li class="row">Relaxon 1 area<span class="fill"></span>£100</li>
    <li class="row">Relaxon 2 areas<span class="fill"></span>£150</li>
    <li class="row">Relaxon 3 areas<span class="fill"></span>£200</li>
    <li class="row">Lip Enhancement 0.5ml<span class="fill"></span>£100</li>
    <li class="row">Lip Enhancement 1ml<span class="fill"></span>£200</li>
    <li class="row">Facial Fillers per 1ml<span class="fill"></span>£200</li>
    <li class="tall"><div class="row">Volumiq per session<span class="fill"></span>£450</div><span class="note">(2 vials - must be bought as a course)</span></li>
    <li class="row">Non Surgical Face Lift (Thread Lift) per area<span class="fill"></span>£600</li>
  </ul>
  <ul class="abs price-list list-right">
    <li class="row">Skin Press Full Face<span class="fill"></span>£250</li>
    <li class="row">Skin Press Small Per Small Area<span class="fill"></span>£100</li>
    <li class="row">Cryo Therapy<span class="fill"></span>£60</li>
    <li class="row">Chemical Peel Light Peel and Microdermabrasion<span class="fill"></span>£85</li>
    <li class="row">Chemical Peel Deep Peel<span class="fill"></span>£150</li>
    <li class="row">Consultation redeemable against service<span class="fill"></span>£30</li>
    <li class="tall"><div class="row">Relaxon Top Up Relaxon<span class="fill"></span>£50</div><span class="note">(must be within 2 weeks of 1st treatment)</span></li>
    <li class="tall"><div class="row">Filler Top Up<span class="fill"></span>£100</div><span class="note">(must be within 2 weeks of 1st appointment)</span></li>
  </ul>

  <h2 class="abs tab tab-hours">Opening Times</h2>
  <ul class="abs price-list hours-left">
    <li class="row">Monday<span class="fill" style="flex:0 0 50px"></span>10am-4pm</li>
    <li class="row">Tuesday<span class="fill" style="flex:0 0 48px"></span>10am-4pm</li>
    <li class="row">Wednesday<span class="fill" style="flex:0 0 30px"></span>12pm-8pm</li>
    <li class="tall"><div class="row">Thursday<span class="fill" style="flex:0 0 36px"></span>7:30am-4:30pm</div><span class="note">(at number 1 Aldwyn Street only)</span></li>
  </ul>
  <ul class="abs price-list hours-right">
    <li class="row">Friday<span class="fill"></span>10am-2pm</li>
    <li class="row">Saturday<span class="fill"></span>9am-2pm</li>
    <li class="row">Sunday<span class="fill"></span>Closed</li>
  </ul>

  <figure class="abs results">
    <div class="results-labels"><span>BEFORE</span><span>DAY 7</span><span>DAY 90</span><span>DAY 120</span></div>
    <div class="results-photo" role="img" aria-label="Before and after treatment photos of a woman's forehead over 120 days"></div>
  </figure>

  <div class="abs map" role="img" aria-label="Street map showing the clinic location"></div>

  <footer class="abs footer">
    <div class="abs contact c-phone">
      <svg width="11" height="11" viewBox="0 0 24 24"><path fill="var(--teal)" d="M6.6 10.8a15 15 0 0 0 6.6 6.6l2.2-2.2c.3-.3.7-.4 1-.2 1.1.4 2.3.6 3.6.6.6 0 1 .4 1 1V20c0 .6-.4 1-1 1A17 17 0 0 1 3 4c0-.6.4-1 1-1h3.5c.6 0 1 .4 1 1 0 1.3.2 2.5.6 3.6.1.3 0 .7-.2 1z"/></svg>
      0208 947 2186
    </div>
    <div class="abs contact c-address">
      <svg width="11" height="13" viewBox="0 0 24 28"><path fill="var(--teal)" d="M12 0a9 9 0 0 0-9 9c0 7 9 19 9 19s9-12 9-19a9 9 0 0 0-9-9zm0 12.5A3.5 3.5 0 1 1 12 5.5a3.5 3.5 0 0 1 0 7z"/></svg>
      <span>482 Pellbrook Road, 6 Warnford High Street, KT4 3JQ</span>
    </div>
    <div class="abs contact c-web">
      <svg width="12" height="12" viewBox="0 0 24 24"><circle cx="12" cy="12" r="10" fill="none" stroke="var(--teal)" stroke-width="2.5"/><path d="M2 12h20M12 2c4 4 4 16 0 20M12 2c-4 4-4 16 0 20" fill="none" stroke="var(--teal)" stroke-width="2"/></svg>
      www.hollyvanmereaesthetics.co.uk
    </div>
    <div class="abs contact c-mail">
      <svg width="12" height="10" viewBox="0 0 24 18"><rect width="24" height="18" rx="2" fill="var(--teal)"/><path d="M1 2l11 8 11-8" fill="none" stroke="var(--header-bottom)" stroke-width="2"/></svg>
      hvmwarnfordbookings@mailbox.com
    </div>
  </footer>
</main>
</body>
</html>
```